Law firm needs stationary and envelope design*

We would like to incorporate our logo into letterhead design and envelopes. We are looking for something that is moderately conservative but not old law firm style. Both the envelopes and the letterhead must have both firm addresses. We would like to incorporate the color of the logo, but only a small amount of color - perhaps on one of the borders. The addresses for the firm locations are listed below. Given that it is a law firm, it needs to somewhat conservative, but not the old school, small black font on cream colored paper design.

The firm addresses are:

27815 N. Harlow Pemberton Pkwy.
Ste 740
Scottsdale, AZ 85419

6208 E. Juniper Street
Ste 820
Burbank, CA 91873

Legal

Designer to choose colors to be used in the design.

• Both addresses:
• 27815 N. Harlow Pemberton Pkwy.
• Ste 740
• Scottsdale, AZ 85419
• 6208 E. Juniper Street
• Ste 820
• Burbank, CA 91873
• Small amount of color on border(s) that matches the logo but not too much color

```html
<!DOCTYPE html>
<html lang="en">
<head>
<meta charset="utf-8">
<title>Castell Law Stationery</title>
<link href="https://fonts.googleapis.com/css2?family=Marcellus&family=Open+Sans:wght@400&display=swap" rel="stylesheet">
<style>
  :root {
    --backdrop: #c4c4c4;
    --paper: #f7f1e2;
    --paper-edge: #e9e1cd;
    --navy: #2a2857;
    --ink: #3a3a44;
  }
  html, body {
    margin: 0;
    padding: 0;
    width: 1200px;
    height: 1199px;
    overflow: hidden;
    background: var(--backdrop);
  }
  .stationery-set {
    position: relative;
    width: 1200px;
    height: 1199px;
  }
  .sheet {
    position: absolute;
    background: var(--paper);
    overflow: hidden;
  }
  .letterhead {
    left: 135px;
    top: 288px;
    width: 453px;
    height: 639px;
  }
  .envelope-back {
    left: 638px;
    top: 451px;
    width: 456px;
    height: 227px;
  }
  .envelope-front {
    left: 638px;
    top: 702px;
    width: 456px;
    height: 227px;
  }
  .firm-name {
    position: absolute;
    margin: 0;
    font-family: "Marcellus", serif;
    font-weight: 400;
    font-size: 20px;
    letter-spacing: 0.3px;
    color: var(--navy);
    white-space: nowrap;
    line-height: 1;
  }
  .letterhead .firm-name {
    left: 0;
    right: 0;
    top: 33px;
    text-align: center;
  }
  .envelope-front .firm-name {
    left: 17px;
    top: 19px;
  }
  .office-addresses {
    position: absolute;
    margin: 0;
    font-family: "Open Sans", sans-serif;
    font-size: 5.4px;
    color: var(--ink);
    white-space: nowrap;
    line-height: 1;
  }
  .letterhead .office-addresses {
    left: 0;
    right: 0;
    bottom: 27px;
    text-align: center;
  }
  .envelope-front .office-addresses {
    left: 17px;
    bottom: 15px;
  }
  .border-band {
    position: absolute;
    left: 0;
    right: 0;
    bottom: 0;
    height: 9px;
    background: var(--navy);
  }
  .envelope-flap {
    position: absolute;
    inset: 0;
  }
</style>
</head>
<body>
  <main class="stationery-set">
    <section class="sheet letterhead" aria-label="Letterhead">
      <h1 class="firm-name">CASTELL LAW</h1>
      <p class="office-addresses">27815 N. Harlow Pemberton Pkwy. Ste 740, Scottsdale, AZ 85419 | 6208 E. Juniper Street Ste 820, Burbank, CA 91873</p>
      <div class="border-band"></div>
    </section>

    <section class="sheet envelope-back" aria-label="Envelope back">
      <svg class="envelope-flap" width="456" height="227" viewBox="0 0 456 227" aria-hidden="true">
        <path d="M1 1 L8 24 Q11 32 20 35 L205 96 Q222 101 240 98 L437 34 Q446 30 450 22 L455 1"
              fill="none" stroke="var(--paper-edge)" stroke-width="1.2"/>
      </svg>
    </section>

    <section class="sheet envelope-front" aria-label="Envelope front">
      <h2 class="firm-name">CASTELL LAW</h2>
      <p class="office-addresses">27815 N. Harlow Pemberton Pkwy. Ste 740, Scottsdale, AZ 85419 | 6208 E. Juniper Street Ste 820, Burbank, CA 91873</p>
      <div class="border-band"></div>
    </section>
  </main>
</body>
</html>
```